Tree Pruning Website

We need a website for a tree Arborist, pruning company called Hollow Ridge Groundcare. We look after all types of trees, knock down trees and prune trees. Our target market is from domestic clients to government clients and everything in between.

We would like to see the use of our main colours which are orange and green

We are not looking forward in seeing a template that we have seen before but a unique template. We have designed 5 templates ourselves and we wish for the design community to take our designs to the next level.

We have also designed a template for things that **we are not** looking for (Version 4)

To make it fair for everyone, we are also not giving out any participation payments as we have had. One winner will take all of the payment!!!

I Have attached a image of the designs and a image of a tree.

We are just looking at the PSD file been developed. We have our own team who can slice the image up into a HTML format.

Target Market(s)

Everyone who needs to cut down a tree

Industry/Entity Type

Government

Requirements
Must have
• Logo on front page
A List of our services
jQuery slider on page
Phone Number on every page

```html
<!DOCTYPE html>
<html lang="en">
<head>
<meta charset="utf-8">
<title>Hollow Ridge Groundcare</title>
<link href="https://fonts.googleapis.com/css2?family=Ubuntu:wght@400;500&family=PT+Sans:wght@400;700&family=Lora:ital@1&display=swap" rel="stylesheet">
<style>
:root{
  --wood:#8c6b4c;
  --wood-dark:#6f5238;
  --green:#9dc400;
  --green-light:#add800;
  --green-text:#6f9c00;
  --orange:#c45a0c;
  --paper:#fdfbf7;
  --band:#e8f0cc;
  --ink:#1d1d1d;
}
*{box-sizing:border-box;margin:0;padding:0}
html,body{width:1200px;height:1192px;overflow:hidden}
body{position:relative;background:linear-gradient(90deg,var(--wood-dark),var(--wood) 20%,#977554 50%,var(--wood) 80%,var(--wood-dark));font-family:"PT Sans",sans-serif;color:var(--ink)}
.abs{position:absolute}
.call{right:192px;top:14px;color:#fff;font-family:"Ubuntu",sans-serif;font-size:17px}
.call strong{font-size:25px;font-weight:500;margin-left:8px}
.nav{left:186px;top:60px;width:825px;height:80px;background:var(--green);display:flex;align-items:center}
.brand{width:202px;padding-left:18px;display:flex;align-items:center;gap:12px;color:#fff;font-family:"Ubuntu",sans-serif;font-size:16px;line-height:1.2}
.brand i{width:14px;height:14px;border-radius:50%;background:#fff;flex:none}
.menu{display:flex;height:100%;list-style:none;font-family:"Ubuntu",sans-serif;font-size:13.5px;color:#fff}
.menu li{display:flex;align-items:center;padding:0 16.5px}
.menu li.active{background:var(--green-light);color:#111;padding:0 17px}
.main{left:187px;top:155px;width:824px;height:1006px;background:var(--paper)}
.hero{left:0;top:14px;width:824px;height:303px;background:linear-gradient(160deg,#c9c3ad 0%,#8c9a6c 40%,#5f7048 70%,#9c9c92 100%)}
.caption{left:26px;top:80px;width:308px;height:189px;background:rgba(240,238,232,.88);padding:28px 10px 0 11px}
.caption h2{font-family:"Ubuntu",sans-serif;font-weight:400;color:var(--orange);font-size:25px;margin-bottom:14px}
.caption p{font-size:13.4px;line-height:19px}
.dots{left:668px;top:279px;width:139px;height:24px;background:var(--paper);border-radius:4px 4px 0 0;display:flex;justify-content:center;align-items:center;gap:5px}
.dots span{width:12px;height:12px;border-radius:50%;background:var(--green)}
.dots span.on{background:var(--orange)}
.services-title{left:10px;top:338px;font-family:"Ubuntu",sans-serif;font-weight:500;font-size:20px}
.tabs{left:10px;top:375px;width:806px;height:22px;border-bottom:2px solid var(--orange);display:flex;font-family:"Ubuntu",sans-serif;font-weight:500;font-size:11px;list-style:none}
.tabs li{padding:0 8.5px;line-height:22px}
.tabs li.active{background:var(--orange);color:#fff}
.svc-photo{left:10px;top:423px;width:136px;height:91px;background:linear-gradient(135deg,#4f5d2a,#7fa63a 50%,#3d4a24)}
.svc-body{left:156px;top:421px;width:655px}
.svc-body h3{font-family:"Ubuntu",sans-serif;font-weight:400;font-size:13px;color:var(--green-text);margin-bottom:4px}
.svc-body p{font-size:11.4px;line-height:19px}
.more{color:var(--green-text);font-size:11.4px;display:flex;align-items:center;gap:8px}
.band{left:179px;top:704px;width:841px;height:156px;background:var(--band)}
.arrow{top:752px;width:60px;height:60px;border-radius:50%;background:var(--band)}
.thumb{top:726px;width:184px;height:114px;border-radius:2px}
.col{top:890px}
.col h4{font-family:"Ubuntu",sans-serif;font-weight:500;font-size:15px;color:var(--green-text);display:flex;align-items:center;gap:6px;margin-bottom:20px}
.col p,.col li{font-size:11.4px;line-height:19px}
.col ul{list-style:none}
.social li{display:flex;align-items:center;gap:14px;height:38px}
.social i{width:28px;height:28px;background:#dde6ea;border-radius:4px;flex:none}
blockquote{font-family:"Lora",serif;font-style:italic;font-size:12.4px;line-height:19px}
.footer{left:187px;top:1119px;width:824px;height:42px;background:var(--green);color:#fff;font-size:10px;padding:15px 11px}
</style>
</head>
<body>
<div class="abs call">feel free to call us on <strong>08 5550 123</strong></div>

<header class="abs nav">
  <div class="brand"><i></i><span>Hollow Ridge<br>Groundcare</span></div>
  <ul class="menu">
    <li class="active">HOME</li><li>ABOUT US</li><li>OUR SERVICES</li><li>GET A QUOTE</li><li>OUR WORK</li><li>CONTACT US</li>
  </ul>
</header>

<main class="abs main">
  <div class="abs hero" role="img" aria-label="Photo looking up into pale-barked gum tree branches against the sky"></div>
  <div class="abs caption">
    <h2>Title Goes Here</h2>
    <p>Lorem ipsum dolor sit amet, consectetur adipisc-ing elit. Aliquam sodales lacus at turpis scelerisque eu ullamcorper enim mattis. Quisque ultrices, neque et blandit rhoncus, ante magna commodo</p>
  </div>
  <div class="abs dots"><span></span><span></span><span class="on"></span><span></span><span></span><span></span></div>

  <h2 class="abs services-title">OUR SERVICES</h2>
  <ul class="abs tabs">
    <li class="active">DIAGNOSIS</li><li>TREATMENT</li><li>PURNING</li><li>TREE REMOVAL</li><li>STAM REMOVAL</li><li>CABLING &amp; BRACING</li><li>ARBORIST CONSULTS</li><li>TREE PROTECTION</li>
  </ul>
  <div class="abs svc-photo" role="img" aria-label="Close-up photo of a tree trunk with green leaves"></div>
  <div class="abs svc-body">
    <h3>DIAGNOSIS</h3>
    <p>Lorem ipsum dolor sit amet, consectetur adipisicing elit, sed do eiusmod tempor incididunt ut labore et dolore magna aliqua. Ut enim ad minim veniam, quis nostrud exercitation ullamco laboris nisi ut aliquip ex ea commodo consequat. Duis aute irure dolor in reprehenderit in voluptate velit esse cillum dolore eu fugiat nulla pariatur.</p>
    <div class="more" style="margin-top:6px">Read More <svg width="20" height="6"><path d="M0 3H16M14 0L20 3L14 6Z" fill="#6f9c00" stroke="#6f9c00" stroke-width="1"/></svg></div>
  </div>

  <section class="abs col" style="left:16px;width:200px;top:735px">
    <h4><svg width="12" height="18"><path d="M6 0L11 14H1Z" fill="#6f9c00"/><rect x="5" y="13" width="2" height="5" fill="#6f9c00"/></svg>About Tree Pruning</h4>
    <p>Duis eu laoreet nisl. Donec bibendum, nisl non malesuada suscipit, dui erat porttitor erat, et congue nunc tellus ac augue. Maecenas sollicitudin vulputate</p>
    <div class="more" style="margin:12px 0 0 101px">Read More <svg width="20" height="6"><path d="M0 3H16M14 0L20 3L14 6Z" fill="#6f9c00" stroke="#6f9c00" stroke-width="1"/></svg></div>
  </section>
  <section class="abs col" style="left:222px;width:200px;top:735px">
    <h4><svg width="12" height="18"><path d="M6 0L11 14H1Z" fill="#6f9c00"/><rect x="5" y="13" width="2" height="5" fill="#6f9c00"/></svg>Follow Us</h4>
    <ul class="social" style="margin-top:-4px">
      <li><i></i>Folow Us On Chirper</li><li><i></i>Check Us Out on Snapline</li><li><i></i>Become a Fan on Friendbook</li>
    </ul>
  </section>
  <section class="abs col" style="left:430px;width:180px;top:735px">
    <h4><svg width="12" height="18"><path d="M6 0L11 14H1Z" fill="#6f9c00"/><rect x="5" y="13" width="2" height="5" fill="#6f9c00"/></svg>Our Services</h4>
    <ul style="padding-left:20px">
      <li>Diagnosis</li><li>Treatment</li><li>Purning</li><li>Tree Removal</li><li>Stam Removal</li><li>Cabling &amp; Bracing</li><li>Arborist Consults</li><li>Tree Protection</li>
    </ul>
  </section>
  <section class="abs col" style="left:630px;width:185px;top:735px">
    <h4><svg width="12" height="18"><path d="M6 0L11 14H1Z" fill="#6f9c00"/><rect x="5" y="13" width="2" height="5" fill="#6f9c00"/></svg>Testimonial</h4>
    <blockquote style="padding-left:30px;position:relative"><span style="position:absolute;left:0;top:-6px;font-size:28px;color:#555">&ldquo;</span>Lorem ipsum dolor sit amet, consectetur adipisicing elit, sed do eiusmod tempor incididunt ut labore et dolore magna aliqua.</blockquote>
    <p style="text-align:right;font-family:'Lora',serif;font-style:italic;font-weight:700;margin-top:10px">~ Marisol</p>
  </section>
</main>

<div class="abs band"></div>
<div class="abs arrow" style="left:154px"><svg class="abs" style="left:12px;top:22px" width="12" height="16"><path d="M9 2L3 8L9 14" fill="none" stroke="#fff" stroke-width="3"/></svg></div>
<div class="abs arrow" style="left:986px"><svg class="abs" style="left:36px;top:22px" width="12" height="16"><path d="M3 2L9 8L3 14" fill="none" stroke="#fff" stroke-width="3"/></svg></div>
<div class="abs band" style="left:179px;width:0"></div>
<div class="abs thumb" style="left:197px;background:linear-gradient(#c8c8c0,#8e9a6a 55%,#4f6a25)" role="img" aria-label="Wooden tree sculpture in a misty field"></div>
<div class="abs thumb" style="left:404px;background:linear-gradient(135deg,#6f9c2a,#3f5a1c 50%,#8bc045)" role="img" aria-label="Branches of a tree with bright green leaves"></div>
<div class="abs thumb" style="left:611px;background:linear-gradient(#4a6a2a,#5f8a30 50%,#8ec43c)" role="img" aria-label="Weeping tree over a striped lawn"></div>
<div class="abs thumb" style="left:818px;background:linear-gradient(90deg,#b8b8ae,#8e9a6a 55%,#d6c49a)" role="img" aria-label="Close view of a wooden tree sculpture in a field"></div>

<footer class="abs footer">Copyright hollowridgecare.com © 2013</footer>
</body>
</html>
```